Keys to business success

I love the principles of a book called "Where the quiet rivers bend toward home". I use the principles all the time at work. I'd like a poster made (map or web style design) to capture the books reminders. You can see a very basic verison of the design i'm looking for attached below "project summary".I've attached a word document of the text to include. Ive also attached two examples of the types of designs i'm looking for. The design will have to look modern and clear when printed on an 45.7 x 61 cm canvas.

Target Market(s)

Buisness people
Motivation

Industry/Entity Type

Business

Font styles to use
Serif

Requirements
Must have
• Web or map-like designs
• All 30 of the principles: 3 fonts (Title, sub-title and principles). The choice of fonts is up to the designer. No numbers for the principles.
• Professional feel
Nice to have
• Halos around phrases
Should not have
• No straight lines or ridgid concepts

```html
<!DOCTYPE html>
<html lang="en">
<head>
<meta charset="utf-8">
<title>30 Principles · Where the Quiet Rivers Bend Toward Home</title>
<link rel="stylesheet" href="https://fonts.googleapis.com/css2?family=Bebas+Neue&family=Nunito:wght@800;900&family=Roboto+Condensed:wght@500;700&display=swap">
<style>
  :root{
    --teal:#3aa3b4;
    --teal-deep:#12627a;
    --navy:#101c36;
    --suit:#1a2743;
    --sunset:#f4c76b;
    --ember:#e58a3a;
    --skin:#e3b596;
    --cream:#f4efc4;
    --white:#ffffff;
    --sky-blue:#1f8fde;
    --cyan:#2fc6f0;
    --ink:#1b2236;
    --dot-gold:#e9e3a6;
    --dot-orange:#f08a2a;
    --dot-blue:#2a9de6;
    --dot-dark:#1a5fa8;
  }
  *{box-sizing:border-box;margin:0;padding:0}
  html,body{width:1200px;height:899px;overflow:hidden;background:var(--navy)}
  .poster{position:relative;width:1200px;height:899px;overflow:hidden;font-family:"Roboto Condensed",Arial,sans-serif}
  .backdrop{
    position:absolute;inset:0;
    background:
      radial-gradient(ellipse 260px 330px at 700px 560px, rgba(227,181,150,.85), rgba(227,181,150,0) 70%),
      radial-gradient(ellipse 170px 210px at 560px 470px, rgba(236,200,170,.7), rgba(236,200,170,0) 70%),
      radial-gradient(ellipse 90px 200px at 870px 230px, rgba(230,190,165,.8), rgba(230,190,165,0) 75%),
      radial-gradient(ellipse 560px 330px at 170px 860px, var(--sunset), rgba(244,199,107,0) 75%),
      radial-gradient(ellipse 420px 260px at 420px 520px, rgba(229,138,58,.55), rgba(229,138,58,0) 70%),
      linear-gradient(90deg, var(--teal) 0%, #2f8aa2 38%, var(--teal-deep) 58%, var(--suit) 75%, var(--navy) 100%);
  }
  .links{position:absolute;inset:0}
  .links path{fill:none;stroke-width:4;stroke-linecap:round;stroke-dasharray:0 10}
  .links .gold{stroke:var(--dot-gold)}
  .links .orange{stroke:var(--dot-orange)}
  .links .blue{stroke:var(--dot-blue)}
  .links .dark{stroke:var(--dot-dark)}
  .links .white{stroke:#bfe4f4}

  .hub{position:absolute;border-radius:50%;display:flex;align-items:center;justify-content:center;text-align:center;
       transform:translate(-50%,-50%);left:var(--x);top:var(--y);width:var(--d);height:var(--d);
       font-family:"Nunito",Arial,sans-serif;font-weight:900;font-size:19px;line-height:24px;color:var(--white)}
  .hub--glow{background:radial-gradient(circle at 50% 45%, #6fd8ff, #1aa0ee 55%, #0b6fc2 100%);
       box-shadow:0 0 22px rgba(120,210,255,.8)}
  .hub--glow span{-webkit-text-stroke:1px var(--navy);paint-order:stroke fill;text-shadow:0 0 2px var(--navy)}
  .hub--night{background:radial-gradient(circle at 55% 70%, rgba(200,220,255,.85), #1f4fa8 45%, #0c1f5a 100%);
       border:2px solid #3b8fe8;box-shadow:0 0 18px rgba(60,140,240,.7)}
  .hub--night span{-webkit-text-stroke:1px var(--navy);paint-order:stroke fill}
  .hub--ring{border:1.5px solid rgba(70,170,240,.9);box-shadow:0 0 10px rgba(120,200,255,.5), inset 0 0 10px rgba(120,200,255,.35)}
  .hub--ring.warm span{color:var(--sky-blue);-webkit-text-stroke:.6px #0d3f7a}
  .hub--ring.cool span{color:#e6f4ff;-webkit-text-stroke:1px #0c3a7a;paint-order:stroke fill}

  .title{position:absolute;left:614px;top:390px;transform:translate(-50%,-50%);white-space:nowrap;
       font-family:"Bebas Neue",Impact,sans-serif;font-size:45px;letter-spacing:-.3px;color:var(--white);
       -webkit-text-stroke:2px #15304c;paint-order:stroke fill;text-shadow:2px 3px 0 #0d2136}

  .principle{position:absolute;left:var(--x);top:var(--y);transform:translate(-50%,-50%);text-align:center;white-space:nowrap;
       font-size:13.5px;line-height:16.5px;font-weight:700}
  .principle--cream{color:var(--cream)}
  .principle--white{color:var(--white)}
  .principle--blue{color:var(--sky-blue)}
  .principle--cyan{color:var(--cyan)}
  .principle--ink{color:var(--ink)}
</style>
</head>
<body>
<main class="poster">
  <div class="backdrop" role="img" aria-label="Photograph of a businessman in a dark suit pointing a finger toward the viewer, set against a teal sky and warm sunset glow"></div>

  <svg class="links" width="1200" height="899" viewBox="0 0 1200 899" aria-hidden="true">
    <path class="gold" d="M208 92 Q228 110 236 128"/>
    <path class="gold" d="M432 190 Q470 170 488 150"/>
    <path class="gold" d="M196 268 Q220 240 246 226"/>
    <path class="orange" d="M398 266 Q430 300 450 340"/>
    <path class="orange" d="M488 424 Q470 480 420 560"/>
    <path class="orange" d="M872 278 Q850 300 834 330"/>
    <path class="orange" d="M820 424 Q840 480 860 520"/>
    <path class="white" d="M812 76 Q840 90 862 110"/>
    <path class="white" d="M735 180 Q770 166 796 180"/>
    <path class="dark" d="M1030 118 Q1000 140 950 158"/>
    <path class="dark" d="M1060 212 Q1010 212 962 208"/>
    <path class="white" d="M968 274 Q990 290 1000 300"/>
    <path class="blue" d="M318 508 L318 560"/>
    <path class="blue" d="M230 530 Q250 550 262 575"/>
    <path class="blue" d="M410 520 Q390 540 380 556"/>
    <path class="blue" d="M462 580 Q430 590 402 610"/>
    <path class="blue" d="M180 600 Q205 606 226 614"/>
    <path class="blue" d="M452 660 L404 660"/>
    <path class="blue" d="M176 664 Q200 658 230 654"/>
    <path class="blue" d="M446 712 Q420 704 400 694"/>
    <path class="blue" d="M176 752 Q220 730 246 712"/>
    <path class="blue" d="M406 786 Q390 760 372 736"/>
    <path class="blue" d="M236 806 Q252 770 262 738"/>
    <path class="blue" d="M336 812 L336 744"/>
    <path class="blue" d="M900 518 Q900 560 892 576"/>
    <path class="blue" d="M760 584 Q790 580 820 606"/>
    <path class="blue" d="M990 592 Q966 610 944 626"/>
    <path class="blue" d="M1030 650 L946 650"/>
    <path class="blue" d="M1040 722 Q1010 716 984 712"/>
    <path class="blue" d="M752 690 Q780 676 812 666"/>
    <path class="blue" d="M966 790 Q960 740 946 716"/>
    <path class="blue" d="M826 808 Q830 760 852 722"/>
  </svg>

  <div class="hub hub--glow" style="--x:330px;--y:196px;--d:186px"><span>Fundamental<br>Techniques<br>in<br>Handling<br>People</span></div>
  <div class="hub hub--night" style="--x:880px;--y:190px;--d:148px"><span>Making<br>People<br>Like<br>You</span></div>
  <div class="hub hub--ring warm" style="--x:318px;--y:655px;--d:172px"><span>Win People<br>to<br>Your Way<br>of<br>Thinking</span></div>
  <div class="hub hub--ring cool" style="--x:877px;--y:648px;--d:138px"><span>Being<br>a<br>Leader</span></div>

  <h1 class="title">30 Principles · Where the Quiet Rivers Bend Toward Home</h1>

  <p class="principle principle--cream" style="--x:168px;--y:64px">Don't Criticize,<br>Condemn<br>or<br>Complain</p>
  <p class="principle principle--cream" style="--x:515px;--y:114px">Arouse In The<br>Other Person<br>An Eager Want</p>
  <p class="principle principle--cream" style="--x:180px;--y:295px">Give Honest,<br>Sincere,<br>Appreciation</p>

  <p class="principle principle--white" style="--x:749px;--y:71px">A Person's Name<br>Is To That Person<br>The Sweetest<br>And Most<br>Important Sound</p>
  <p class="principle principle--white" style="--x:1030px;--y:72px">Be A Good Listener.<br>Encourage Others<br>To Talk<br>About Themselves</p>
  <p class="principle principle--white" style="--x:697px;--y:189px">Smile</p>
  <p class="principle principle--white" style="--x:1083px;--y:226px">Talk In Terms<br>Of The Other<br>Person's Interests</p>
  <p class="principle principle--white" style="--x:752px;--y:293px">Become Genuinely<br>Interested<br>In<br>Other People</p>
  <p class="principle principle--white" style="--x:1033px;--y:328px">Make The Other<br>Person Feel Important<br>- And Do It Sincerely</p>

  <p class="principle principle--blue" style="--x:320px;--y:460px">Throw<br>Down A<br>Challenge</p>
  <p class="principle principle--blue" style="--x:213px;--y:494px">The Only Way<br>To Get<br>The Best Of An<br>Argument Is To Avoid It</p>
  <p class="principle principle--blue" style="--x:425px;--y:494px">Dramatize<br>Your<br>Ideas</p>
  <p class="principle principle--blue" style="--x:496px;--y:556px">Appeal To<br>The<br>Nobler Motives</p>
  <p class="principle principle--blue" style="--x:112px;--y:562px">Show Respect For<br>The Other Person's<br>Opinion. Never Say,<br>"You're Wrong."</p>
  <p class="principle principle--blue" style="--x:522px;--y:639px">Be Sympathetic<br>With The Other<br>Person's Ideas<br>And Desires</p>
  <p class="principle principle--blue" style="--x:101px;--y:664px">If You Are Wrong<br>Admit It<br>Quickly<br>And<br>Emphatically</p>
  <p class="principle principle--blue" style="--x:519px;--y:725px">Try Honestly<br>To See Things<br>From The Other<br>Person's Point Of View</p>
  <p class="principle principle--blue" style="--x:122px;--y:758px">Begin In<br>A<br>Friendly<br>Manner</p>
  <p class="principle principle--blue" style="--x:471px;--y:809px">Let The Other Person<br>Feel That The Idea<br>Is His Or Hers</p>
  <p class="principle principle--blue" style="--x:198px;--y:830px">Get The Other<br>Person Saying<br>"Yes, Yes"</p>
  <p class="principle principle--blue" style="--x:335px;--y:850px">Let The Other<br>Person Do A Great<br>Deal Of The Talking</p>

  <p class="principle principle--cyan" style="--x:903px;--y:472px">Begin With Praise<br>And Honest<br>Appreciation</p>
  <p class="principle principle--ink" style="--x:750px;--y:516px">Call Attention<br>To People's<br>Mistakes Indirectly</p>
  <p class="principle principle--cyan" style="--x:1047px;--y:546px">Make The Other<br>Person Happy<br>About Doing<br>The Thing<br>You Suggest</p>
  <p class="principle principle--ink" style="--x:708px;--y:635px">Talk About Your<br>Own Mistakes Before<br>Criticizing The<br>Other Person</p>
  <p class="principle principle--cyan" style="--x:1104px;--y:634px">Use Encouragement.<br>Make The Fault<br>Seem Easy To Correct</p>
  <p class="principle principle--cyan" style="--x:1088px;--y:745px">Give The Other<br>Person A Fine<br>Reputation<br>To Live Up To</p>
  <p class="principle principle--ink" style="--x:737px;--y:751px">Ask Questions<br>Instead Of Giving<br>Direct Orders</p>
  <p class="principle principle--cyan" style="--x:976px;--y:828px">Praise The Slightest<br>Improvement<br>And Praise<br>Every Improvement.</p>
  <p class="principle principle--cyan" style="--x:801px;--y:831px">Let The Other<br>Person Save Face</p>
</main>
</body>
</html>
```